Scrum Master & Agile IT Coach Needing Business Website

Hello, my name is Brent Ellison
I am a project manger, scrum master, & agile coach. I work with IT development teams on major projects for Fortune 500 companies . My project management business has a website and can be found here: www.tq-steadfast.example

I have launched a new company, ALL focused on IT Agile Coaching, I am looking to have a website created for my new company - the name of the new company is: Pins and Pegs - Agile IT Coaching and Training.
I have a logo and it is provided in the materials. I like to logo; I am open to different color pallets.

The website will have a total of 7 pages; I have content for 5 of the 7 pages prepared; the other 2 pages will say under construction.

Page 1 Who am I, What I do, My Experience
Demonstrated experience and progression from Scrum Master to
Program Manager to Coach

Page 2 Pins & Pegs - Agile Team Coaching
teams working major IT projects, multiple months/years

Page 3 Coaching @ the Team Level

Page 4 Coaching @ the Program Level ; ScaleFlow ART level

Pages 5 -6 Under Construction

Page 7 Presentations, Slide Decks, Reference Materials

Mentors Nook need to have this highlighted somewhere Monthly Blog
Updates

Industry/Entity Type

IT development

Coding

Coded - Design and coding required

Number of Pages Required

5+ page

Requirements
Must have
• the website must be bold - I want those who visit to remember coming to my coaching site
Nice to have
• nice to have will be a modern / futuristic website; I work with IT developers, I want a website they will like
Should not have
• should not be stiff - it should be professional but fun

```html
<!DOCTYPE html>
<html lang="en">
<head>
<meta charset="utf-8">
<title>Pins &amp; Pegs - Coaching @ the Team Level</title>
<link rel="stylesheet" href="https://fonts.googleapis.com/css2?family=Roboto:wght@400;500;700;900&family=Ubuntu:wght@500;700&family=Barlow+Semi+Condensed:wght@600;700&display=swap">
<style>
  :root{
    --navy:#0c1a2b;
    --brand:#2f5fa3;
    --blue:#4a88cc;
    --blue-mid:#3a6fb0;
    --blue-text:#3a5f9a;
    --teal:#3d7f79;
    --ice:#e9f1fa;
    --card-line:#a9c6ea;
    --btn:#4a6f9a;
    --footer:#333639;
    --white:#ffffff;
  }
  *{box-sizing:border-box;margin:0;padding:0}
  html,body{width:1200px;height:4093px;overflow:hidden;background:var(--white)}
  body{position:relative;font-family:"Roboto",sans-serif;color:var(--blue-text)}

  .brand{position:absolute;display:flex;align-items:center;gap:10px;font-family:"Roboto",sans-serif;font-weight:900;color:var(--brand);white-space:nowrap}
  .brand .dot{width:18px;height:18px;border-radius:50%;background:var(--brand)}
  .brand-box{position:absolute;background:var(--white);border-radius:8px}

  .site-header{position:absolute;left:0;top:0;width:1200px;height:88px;background:var(--white)}
  .site-header .brand{left:111px;top:24px;font-size:28px}
  .nav{position:absolute;top:32px;left:0;width:1200px;height:24px}
  .nav a{position:absolute;font-family:"Roboto",sans-serif;font-weight:700;font-size:15px;color:#1d1d1d;text-decoration:none;text-shadow:0 1px 2px rgba(0,0,0,.25)}

  .hero{position:absolute;left:0;top:88px;width:1200px;height:397px}
  .hero-panel{position:absolute;left:0;top:0;width:500px;height:397px;background:var(--navy)}
  .hero-title{position:absolute;left:0;top:86px;width:530px;text-align:center;font-family:"Roboto",sans-serif;font-weight:900;font-size:56px;line-height:62px;color:var(--white)}
  .hero-photo{position:absolute;left:500px;top:0;width:700px;height:397px;background:linear-gradient(120deg,#e9e6e2 0%,#c9c3bc 45%,#8a8f99 75%,#f1f0ee 100%)}

  .values{position:absolute;left:0;top:485px;width:1200px;height:758px;background:var(--white)}
  .values .brand{left:119px;top:97px;font-size:22px}
  .values-blob{position:absolute;left:152px;top:210px;width:334px;height:326px}
  .btn{position:absolute;display:flex;align-items:center;justify-content:center;color:var(--white);font-family:"Roboto",sans-serif;font-weight:700;border-radius:30px;letter-spacing:1.5px}
  .btn-learn{left:257px;top:630px;width:174px;height:58px;background:var(--btn);font-size:17px}
  .value-item{position:absolute;left:638px;width:460px;height:62px;display:flex;align-items:center}
  .value-item svg{flex:none}
  .value-item p{margin-left:37px;font-weight:700;font-size:17.5px;line-height:22px;color:var(--blue-mid)}

  .principles{position:absolute;left:0;top:1243px;width:1200px;height:944px;background:var(--ice)}
  .principles .brand-box{left:94px;top:23px;width:276px;height:90px}
  .principles .brand{left:132px;top:52px;font-size:25px}
  .principles h2{position:absolute;left:430px;top:42px;font-family:"Barlow Semi Condensed",sans-serif;font-weight:700;font-size:46px;color:var(--teal)}
  .card{position:absolute;width:248px;height:183px;background:var(--white);border:1.5px solid var(--card-line);border-radius:22px;display:flex;align-items:center;justify-content:center;padding:10px 14px;text-align:center;font-size:17px;line-height:22px;color:var(--blue-text)}

  .team{position:absolute;left:0;top:2187px;width:1200px;height:832px;background:linear-gradient(180deg,#f4f8fd 0%,#c9dcf2 55%,#9ebfe7 100%)}
  .team .brand-box{left:49px;top:50px;width:323px;height:91px}
  .team .brand{left:90px;top:82px;font-size:27px}
  .team-card{position:absolute;left:262px;top:130px;width:675px;height:663px;background:var(--white);border-radius:42px}
  .team-dot{position:absolute;left:400px;top:112px;width:74px;height:74px;border-radius:50%;background:var(--blue)}
  .team h2{position:absolute;left:400px;top:200px;font-family:"Ubuntu",sans-serif;font-weight:700;font-size:41px;line-height:44px;color:var(--blue)}
  .team-art{position:absolute;left:774px;top:160px;width:370px;height:350px;border-radius:50% 50% 50% 10%;background:linear-gradient(140deg,#ede9f7 0%,#d3cbee 50%,#b8abe0 100%)}
  .team-list{position:absolute;left:400px;top:382px;width:440px;text-align:center;list-style:none;font-family:"Ubuntu",sans-serif;font-weight:500;font-size:16.5px;line-height:29px;color:var(--blue-mid)}
  .btn-read{left:547px;top:708px;width:136px;height:37px;background:#3d73b9;font-size:13px;letter-spacing:.8px}

  .program{position:absolute;left:0;top:3019px;width:1200px;height:827px;background:linear-gradient(180deg,#e6eff9 0%,#b9d1ef 50%,#7fa9dc 100%)}
  .program .brand-box{left:83px;top:40px;width:325px;height:90px}
  .program .brand{left:122px;top:72px;font-size:27px}
  .program h2{position:absolute;left:450px;top:40px;width:642px;text-align:center;font-family:"Barlow Semi Condensed",sans-serif;font-weight:700;font-size:44px;line-height:48px;color:#5b92d3}
  .program-photo{position:absolute;left:83px;top:216px;width:495px;height:521px;background:linear-gradient(135deg,#5b4a3f 0%,#a08a78 40%,#dcd6d0 75%,#f3f2f0 100%)}
  .check{position:absolute;left:594px;width:560px;display:flex;align-items:flex-start}
  .check svg{flex:none}
  .check p{margin-left:15px;font-family:"Roboto",sans-serif;font-weight:700;font-size:27px;line-height:33px;color:var(--blue)}

  .site-footer{position:absolute;left:0;top:3846px;width:1200px;height:177px;background:var(--white)}
  .site-footer .brand{left:127px;top:44px;font-size:40px}
  .social{position:absolute;top:9px;width:48px;height:48px;border-radius:50%}
  .field{position:absolute;top:93px;height:42px;border:1px solid #b9b9b9;background:var(--white);font-family:"Roboto",sans-serif;font-size:14px;color:#888;padding:12px 12px}
  .submit{position:absolute;left:1011px;top:93px;width:101px;height:42px;background:#2e74d6;color:var(--white);font-family:"Roboto",sans-serif;font-weight:500;font-size:15px;display:flex;align-items:center;justify-content:center}
  .bottom-bar{position:absolute;left:0;top:4023px;width:1200px;height:70px;background:var(--footer);display:flex;align-items:center;justify-content:center;font-size:12px;color:var(--white)}
  .bottom-bar u{color:#9ec3ff}
</style>
</head>
<body>

<header class="site-header">
  <div class="brand"><span class="dot"></span>Pins &amp; Pegs</div>
  <nav class="nav">
    <a style="left:656px">HOME</a>
    <a style="left:742px">COACH</a>
    <a style="left:834px">CONTACT</a>
    <a style="left:944px">BOOKING</a>
    <a style="left:1056px">BLOG</a>
  </nav>
</header>

<section class="hero">
  <div class="hero-panel"></div>
  <h1 class="hero-title">Coaching @ the<br>Team Level</h1>
  <div class="hero-photo" role="img" aria-label="Photo of an experienced coach and a younger developer working together at a laptop"></div>
</section>

<section class="values">
  <div class="brand"><span class="dot"></span>Pins &amp; Pegs</div>
  <svg class="values-blob" viewBox="0 0 334 326" role="group">
    <path d="M40 70 C90 20 160 60 215 25 C270 -8 335 20 334 85 C333 140 290 170 300 230 C312 300 250 340 195 315 C140 290 120 260 70 250 C15 240 -10 190 5 140 C15 105 20 90 40 70 Z" fill="#4a88cc"/>
    <text x="167" y="148" text-anchor="middle" font-family="Roboto, sans-serif" font-size="66" fill="#fff">Scrum</text>
    <text x="160" y="218" text-anchor="middle" font-family="Roboto, sans-serif" font-size="66" fill="#fff">Values</text>
  </svg>
  <div class="btn btn-learn">LEARN MORE</div>

  <div class="value-item" style="top:104px">
    <svg width="62" height="62" viewBox="0 0 62 62"><circle cx="31" cy="31" r="30" fill="#2f64ad"/><path d="M25 20h12l4 5-10 11-10-11z" fill="none" stroke="#fff" stroke-width="2"/><path d="M17 44h7l6 3h9l7-5" fill="none" stroke="#fff" stroke-width="2"/></svg>
    <p>Customer collaboration over contract<br>negotiation</p>
  </div>
  <div class="value-item" style="top:263px">
    <svg width="62" height="62" viewBox="0 0 62 62"><circle cx="31" cy="31" r="30" fill="#2f64ad"/><path d="M25 20h12l4 5-10 11-10-11z" fill="none" stroke="#fff" stroke-width="2"/><path d="M17 44h7l6 3h9l7-5" fill="none" stroke="#fff" stroke-width="2"/></svg>
    <p>Working software over comprehensive<br>documentation</p>
  </div>
  <div class="value-item" style="top:420px">
    <svg width="62" height="62" viewBox="0 0 62 62"><circle cx="31" cy="31" r="30" fill="#2f64ad"/><path d="M25 20h12l4 5-10 11-10-11z" fill="none" stroke="#fff" stroke-width="2"/><path d="M17 44h7l6 3h9l7-5" fill="none" stroke="#fff" stroke-width="2"/></svg>
    <p>Individuals and interactions over<br>processes and tools</p>
  </div>
  <div class="value-item" style="top:577px">
    <svg width="62" height="62" viewBox="0 0 62 62"><circle cx="31" cy="31" r="30" fill="#2f64ad"/><path d="M25 20h12l4 5-10 11-10-11z" fill="none" stroke="#fff" stroke-width="2"/><path d="M17 44h7l6 3h9l7-5" fill="none" stroke="#fff" stroke-width="2"/></svg>
    <p>Responding to change over following a<br>plan</p>
  </div>
</section>

<section class="principles">
  <div class="brand-box"></div>
  <div class="brand"><span class="dot"></span>Pins &amp; Pegs</div>
  <h2>WE FOLLOW THESE PRINCIPLES</h2>

  <div class="card" style="left:84px;top:152px">Sample Our highest priority is to satisfy the customer through early and continuous delivery of valuable software.</div>
  <div class="card" style="left:346px;top:152px">Welcome changing requirements, even late in development. Agile processes harness change for the customer's competitive advantage.</div>
  <div class="card" style="left:608px;top:152px">Deliver working software frequently, from acouple of weeks to a couple of months, with a preference to the shorter timescale.</div>
  <div class="card" style="left:869px;top:152px">Our highest priority is to satisfy the customer through early and continuous delivery of valuable software.</div>

  <div class="card" style="left:84px;top:351px">Business people and developers must work together daily throughout the project.</div>
  <div class="card" style="left:346px;top:351px">Build projects around motivated individuals. Give them the environment and support they need, and trust them to get the job done.</div>
  <div class="card" style="left:608px;top:351px">The most efficient and effective method of conveying information to and within a development team is face-to-face conversation.</div>
  <div class="card" style="left:869px;top:351px">Working software is the primary measure of progress.</div>

  <div class="card" style="left:84px;top:549px">Agile processes promote sustainable development. The sponsors, developers, and users should be able to maintain a constant pace indefinitely.</div>
  <div class="card" style="left:346px;top:549px">Continuous attention to technical excellence and good design enhances agility.</div>
  <div class="card" style="left:608px;top:549px">Simplicity–the art of maximizing the amount of work not done–is essential.</div>
  <div class="card" style="left:869px;top:549px">The best architectures, requirements, and designs emerge from self-organizing teams.</div>

  <div class="card" style="left:84px;top:746px">At regular intervals, the team reflects on how to become more effective, then tunes and adjusts its behavior accordingly.</div>
</section>

<section class="team">
  <div class="brand-box"></div>
  <div class="brand"><span class="dot"></span>Pins &amp; Pegs</div>
  <div class="team-card"></div>
  <div class="team-dot"></div>
  <h2>Coaching &amp; Running<br>Teams @ the Team<br>Level</h2>
  <div class="team-art" role="img" aria-label="Illustration of a businessman standing beside a large smartphone showing app screens"></div>
  <ul class="team-list">
    <li>Team Working Agreements</li>
    <li>Stakeholder Communications Plans</li>
    <li>Team Words: Honesty, Respect, Transparency,</li>
    <li>Dependability</li>
    <li>Forming Storming, Norming Performing</li>
    <li>Retooling and Sharpening</li>
    <li>Team Member Assessments</li>
    <li>Agile Team Assessments</li>
    <li>Team Retrospectives Project / Program Lessons</li>
    <li>Learned</li>
  </ul>
  <div class="btn btn-read">READ MORE</div>
</section>

<section class="program">
  <div class="brand-box"></div>
  <div class="brand"><span class="dot"></span>Pins &amp; Pegs</div>
  <h2>Coaching @ the Program Level;<br>ScaleFlow ART level</h2>
  <div class="program-photo" role="img" aria-label="Photo of two colleagues reviewing work together at a desk"></div>

  <div class="check" style="top:228px">
    <svg width="78" height="78" viewBox="0 0 78 78"><circle cx="39" cy="39" r="38" fill="#3f7ccb"/><path d="M14 42l17 17 38-42" fill="none" stroke="#fff" stroke-width="7" stroke-linecap="round" stroke-linejoin="round"/></svg>
    <p style="margin-top:22px">Scrum of Scrums</p>
  </div>
  <div class="check" style="top:336px">
    <svg width="78" height="78" viewBox="0 0 78 78"><circle cx="39" cy="39" r="38" fill="#3f7ccb"/><path d="M14 42l17 17 38-42" fill="none" stroke="#fff" stroke-width="7" stroke-linecap="round" stroke-linejoin="round"/></svg>
    <p style="margin-top:20px">Standing up ScaleFlow ART (program<br>level, multiple development<br>teams)</p>
  </div>
  <div class="check" style="top:508px">
    <svg width="78" height="78" viewBox="0 0 78 78"><circle cx="39" cy="39" r="38" fill="#3f7ccb"/><path d="M14 42l17 17 38-42" fill="none" stroke="#fff" stroke-width="7" stroke-linecap="round" stroke-linejoin="round"/></svg>
    <p style="margin-top:20px">Facilitating PI Planning @ the<br>team level</p>
  </div>
</section>

<footer class="site-footer">
  <div class="brand"><span class="dot" style="width:26px;height:26px"></span>Pins &amp; Pegs</div>
  <div class="social" style="left:893px;background:#3b5b9a" role="img" aria-label="Social profile link"></div>
  <div class="social" style="left:950px;background:#2a9be6" role="img" aria-label="Social profile link"></div>
  <div class="social" style="left:1009px;background:#c8338a" role="img" aria-label="Social profile link"></div>
  <div class="social" style="left:1068px;background:#1d70b0" role="img" aria-label="Social profile link"></div>
  <div class="field" style="left:623px;width:180px">Name</div>
  <div class="field" style="left:817px;width:179px">Email</div>
  <div class="submit">Submit</div>
</footer>
<div class="bottom-bar"><span><u>Website Templates</u> created with <u>Website Builder Software</u>.</span></div>

</body>
</html>
```